Business Cards

We are an innovating group of real estate investors who buy beat up house's, fix them up, and resell them. We are in need of a business card that is catchy and stands out. We want it to say something like " We buy house's cash fast" Call us first

Industry/Entity Type

Business

Requirements
Must have
• Our logo which is updated

```html
<!DOCTYPE html>
<html lang="en">
<head>
<meta charset="utf-8">
<title>Hexagon Business Card – Front and Back</title>
<link rel="stylesheet" href="https://fonts.googleapis.com/css2?family=Mulish:wght@400;700;800&display=swap">
<style>
  :root {
    --backdrop: #6e3c1e;
    --card-white: #ffffff;
    --brand-purple: #7a1a8c;
    --brand-lime: #7fd320;
    --brand-green: #1f8a2e;
    --text-dark: #333333;
    --text-grey: #8a8a8a;
    --title-green: #4b8e1a;
  }
  * { margin: 0; padding: 0; box-sizing: border-box; }
  html, body {
    width: 1200px;
    height: 750px;
    overflow: hidden;
    background: var(--backdrop);
  }
  .canvas {
    position: relative;
    width: 1200px;
    height: 750px;
    font-family: "Mulish", Arial, sans-serif;
    color: var(--text-dark);
  }
  .card-shapes {
    position: absolute;
    inset: 0;
  }

  /* Front card */
  .card-front__content {
    position: absolute;
    left: 167px;
    top: 300px;
    width: 396px;
    text-align: center;
  }
  .card-front__mark {
    display: flex;
    align-items: center;
    justify-content: center;
    gap: 12px;
  }
  .card-front__square {
    width: 22px;
    height: 22px;
    background: var(--brand-lime);
  }
  .card-front__name {
    font-weight: 800;
    font-size: 30px;
    letter-spacing: 0.5px;
    color: var(--brand-purple);
  }
  .card-front__rule {
    width: 220px;
    height: 3px;
    margin: 18px auto 16px;
    background: var(--brand-lime);
  }
  .card-front__tagline {
    font-weight: 800;
    font-size: 17px;
    letter-spacing: 1px;
    color: var(--text-dark);
  }
  .card-front__call {
    margin-top: 8px;
    font-weight: 800;
    font-size: 17px;
    letter-spacing: 1px;
    color: var(--title-green);
  }

  /* Back card */
  .card-back__details {
    position: absolute;
    left: 591px;
    top: 254px;
    width: 397px;
    text-align: center;
  }
  .person-name {
    font-weight: 800;
    font-size: 19px;
    letter-spacing: 0.5px;
    color: var(--text-dark);
  }
  .person-title {
    margin-top: 9px;
    font-weight: 800;
    font-size: 15px;
    letter-spacing: 0.5px;
    color: var(--title-green);
  }
  .company-name {
    margin-top: 25px;
    font-weight: 800;
    font-size: 14.5px;
    color: var(--brand-purple);
  }
  .company-name__suffix {
    color: var(--text-grey);
  }
  .address-line,
  .contact-line {
    font-size: 14.5px;
    line-height: 22px;
    color: var(--text-dark);
  }
  .contact-block { margin-top: 15px; }
</style>
</head>
<body>
<main class="canvas">
  <svg class="card-shapes" width="1200" height="750" viewBox="0 0 1200 750" aria-hidden="true">
    <polygon class="card-front" points="365,126 563,258 563,494 365,623 167,494 167,258" fill="var(--card-white)"/>
    <polygon points="789,126 988,258 988,494 789,623 591,494 591,258" fill="var(--brand-purple)"/>
    <clipPath id="upper-half"><rect x="580" y="110" width="420" height="260"/></clipPath>
    <clipPath id="lower-half"><rect x="580" y="370" width="420" height="270"/></clipPath>
    <polygon points="789,138 978,263 978,489 789,611 601,489 601,263" fill="var(--brand-lime)" clip-path="url(#upper-half)"/>
    <polygon points="789,138 978,263 978,489 789,611 601,489 601,263" fill="var(--brand-green)" clip-path="url(#lower-half)"/>
    <polygon points="789,146 971,267 971,485 789,603 608,485 608,267" fill="var(--card-white)"/>
  </svg>

  <section class="card-front__content">
    <div class="card-front__mark">
      <span class="card-front__square"></span>
      <span class="card-front__name">COMPANY NAME</span>
    </div>
    <div class="card-front__rule"></div>
    <p class="card-front__tagline">WE BUY HOUSES · CASH · FAST</p>
    <p class="card-front__call">CALL US FIRST</p>
  </section>

  <section class="card-back__details">
    <p class="person-name">DALE MORROW</p>
    <p class="person-title">DIRECTOR</p>
    <p class="company-name">COMPANY NAME<span class="company-name__suffix">.inc</span></p>
    <div class="address-block">
      <p class="address-line">P O Box 402</p>
      <p class="address-line">Westbrook 4410</p>
    </div>
    <div class="contact-block">
      <p class="contact-line">0800 555 018</p>
      <p class="contact-line">+64 21 555 419</p>
      <p class="contact-line">dale@companyname.com</p>
      <p class="contact-line">companyname.com</p>
    </div>
  </section>
</main>
</body>
</html>
```